HOME IMPROVEMENT Business Card

I want a very unique business card. nothing typical and boring. Im open to you ideas. Ive seen cards with gold and silver or color foil and spot UV coatings. Im looking for something that looks cool and grabs attention. I like rounded corners but am open to all suggestions. We are a home improvement company and I will have a presentation folder printed and a catalog printed also and want to keep that same theme. I love the colors in our logo but I am open at looking at a 3rd color that would work with my logo. I hope that helps.
Card should include
Address
Phone
Fax
Email
Website
Target Market(s)
Home owners, people looking to remodel their home
Industry/Entity Type
Home Improvement
Contact Information for Business Card
2873 Maple Crest Avenue Unit 410
Linden Falls, Il 60284
Phone
Direct Line
Email
Website
Font styles to use
Other font styles liked:
- IM OPEN MINDED
Requirements
Must have
- High end quality look nothing boring I like rounded corners but am open minded
Nice to have
- WOW. I want something nice and impressive.
Should not have
- ??? Not sure

```html
<!DOCTYPE html>
<html lang="en">
<head>
<meta charset="utf-8">
<title>Brickwell Remodeling Group – Business Card</title>
<link href="https://fonts.googleapis.com/css2?family=Roboto:wght@400;500;700&display=swap" rel="stylesheet">
<style>
  :root {
    --navy: #1b2247;
    --green: #0f9a44;
    --card: #ffffff;
    --backdrop: #5d676d;
    --text-muted: #2b3152;
  }
  html, body {
    margin: 0;
    padding: 0;
    width: 1200px;
    height: 900px;
    overflow: hidden;
    background: var(--backdrop);
    font-family: "Roboto", Arial, sans-serif;
  }
  .canvas {
    width: 1200px;
    height: 900px;
    display: flex;
    align-items: center;
    justify-content: center;
    gap: 50px;
  }
  .card {
    position: relative;
    width: 525px;
    height: 300px;
    background: var(--card);
    border-radius: 22px;
    overflow: hidden;
    box-shadow: 0 10px 30px rgba(0,0,0,0.35);
  }

  /* Front face */
  .front .edge-tab {
    position: absolute;
    height: 7px;
    width: 95px;
    background: var(--green);
    border-radius: 4px;
  }
  .front .edge-tab.top { top: 0; left: 40px; }
  .front .edge-tab.bottom { bottom: 0; right: 40px; }
  .front .brand {
    position: absolute;
    top: 100px;
    left: 0;
    right: 0;
    display: flex;
    align-items: center;
    justify-content: center;
    gap: 12px;
  }
  .brand-mark {
    width: 16px;
    height: 16px;
    background: var(--green);
  }
  .brand-name {
    font-weight: 700;
    color: var(--navy);
    font-size: 34px;
    letter-spacing: 0.5px;
  }
  .front .website {
    position: absolute;
    left: 0;
    right: 0;
    bottom: 60px;
    text-align: center;
    font-size: 14px;
    color: var(--navy);
  }

  /* Back face */
  .back .brand {
    position: absolute;
    top: 26px;
    left: 30px;
    display: flex;
    align-items: center;
    gap: 8px;
  }
  .back .brand-mark { width: 10px; height: 10px; }
  .back .brand-name { font-size: 18px; }
  .person {
    position: absolute;
    top: 82px;
    left: 30px;
  }
  .person-name {
    color: var(--green);
    font-size: 17px;
    font-weight: 500;
    letter-spacing: 0.3px;
  }
  .person-role {
    color: var(--navy);
    font-size: 11px;
    margin-top: 2px;
    letter-spacing: 0.5px;
  }
  .divider {
    position: absolute;
    top: 124px;
    left: 30px;
    right: 30px;
    height: 2px;
    background: var(--green);
  }
  .contact-list {
    position: absolute;
    top: 138px;
    left: 30px;
    margin: 0;
    padding: 0;
    list-style: none;
  }
  .contact-list li {
    display: flex;
    align-items: center;
    gap: 8px;
    font-size: 12px;
    color: var(--text-muted);
    line-height: 20px;
  }
  .contact-list svg { width: 10px; height: 10px; fill: var(--green); }
  .address {
    position: absolute;
    right: 30px;
    bottom: 30px;
    text-align: right;
    font-size: 12.5px;
    color: var(--navy);
    line-height: 18px;
  }
</style>
</head>
<body>
<main class="canvas">
  <section class="card front" aria-label="Business card front">
    <span class="edge-tab top"></span>
    <span class="edge-tab bottom"></span>
    <div class="brand">
      <span class="brand-mark"></span>
      <span class="brand-name">Brickwell Remodeling</span>
    </div>
    <div class="website">www.brickwellhome.com</div>
  </section>

  <section class="card back" aria-label="Business card back">
    <div class="brand">
      <span class="brand-mark"></span>
      <span class="brand-name">Brickwell Remodeling</span>
    </div>
    <div class="person">
      <div class="person-name">DORIAN WELLS</div>
      <div class="person-role">FOUNDER</div>
    </div>
    <div class="divider"></div>
    <ul class="contact-list">
      <li><svg viewBox="0 0 10 10"><path d="M2 0h2l1 3-1.5 1a6 6 0 0 0 2.5 2.5L7 5l3 1v2c0 1-1 2-2 2A8 8 0 0 1 0 2c0-1 1-2 2-2z"/></svg>555-318-2046</li>
      <li><svg viewBox="0 0 10 10"><path d="M2.5 0h5a1 1 0 0 1 1 1v8a1 1 0 0 1-1 1h-5a1 1 0 0 1-1-1V1a1 1 0 0 1 1-1zm0 1.5v6h5v-6z"/></svg>555-318-2047</li>
      <li><svg viewBox="0 0 10 10"><path d="M0 2h10v6H0zM1 3v.4l4 2.4 4-2.4V3L5 5.2z"/></svg>dorian@brickwellhome.com</li>
      <li><svg viewBox="0 0 10 10"><circle cx="5" cy="5" r="4.5" fill="none" stroke="#0f9a44" stroke-width="1"/><path d="M0.5 5h9M5 0.5c-2 2.5-2 6.5 0 9M5 0.5c2 2.5 2 6.5 0 9" fill="none" stroke="#0f9a44" stroke-width="0.8"/></svg>www.brickwellhome.com</li>
    </ul>
    <div class="address">
      2873 Maple Crest Avenue Unit 410<br>
      Linden Falls, Il 60284
    </div>
  </section>
</main>
</body>
</html>
```